Wordpress Lifestyle Blog

Just to be clear - I have the domain and the wordpress site (which is messy). I need someone to help me complete a simple blog design and then go into the existing wordpress site, and get rid of all the existing rubbish and set up the templates please. If we progress with design can we please be clear about additional costs upfront which, of course, I appreciate is the case.

Need a lifestyle blog. It is called brightyearsahead.com. Aimed at the older woman but needs to look fresh and young, not old fashioned. Navigation will be Home, Fashion, Feelings, Fitness, Contact. I have a logo but not sure it will work at the moment so happy with stylised words.Will have social media links.

Need homepage (not overly long) to have a main slider for pics/videos. Then the three category boxes underneath linking through to 2nd level pages containing blogs for that category and then the actual blog page. Happy to be led by expertise if this is not gonna work.

Am really looking for something clean and fresh like a Marwyn type approach to be honest.

If you need any further direction please just ask - once design chosen I am looking to move quickly.

Thank you so much for looking at this brief

Target Market(s)

Women, 40 - 60 age group but with a younger outlook

Number of Pages Required

3 page

Colors

Designer to choose colors to be used in the design.

Requirements
Must have
• Reflect youth, fun, bright
• Lift easily into a wordpress format
Should not have
• Old, staid, frumpy,dark

```html
<!DOCTYPE html>
<html lang="en">
<head>
<meta charset="utf-8">
<title>Bright Years Ahead – Lifestyle Blog</title>
<link href="https://fonts.googleapis.com/css2?family=Lato:wght@400;700;900&display=swap" rel="stylesheet">
<style>
  :root {
    --teal: #1b9aa1;
    --teal-dark: #167f85;
    --pink: #d8417f;
    --ink: #2b2b2b;
    --text: #3d3d3d;
    --footer: #262626;
    --white: #ffffff;
    --hero-a: #d9c7a8;
    --hero-b: #b9a58c;
  }
  * { box-sizing: border-box; margin: 0; padding: 0; }
  html, body { width: 780px; height: 1200px; overflow: hidden; background: var(--white); }
  body { font-family: "Lato", Arial, sans-serif; color: var(--text); position: relative; }

  .site-header { position: absolute; top: 0; left: 0; width: 780px; height: 58px; }
  .brand { position: absolute; left: 49px; top: 16px; font-size: 22px; font-weight: 900; color: var(--teal); letter-spacing: -0.5px; }
  .main-nav { position: absolute; right: 48px; top: 24px; display: flex; gap: 29px; }
  .main-nav a { font-size: 9px; font-weight: 700; color: var(--ink); text-decoration: none; letter-spacing: 0.2px; }
  .main-nav a.is-current { color: var(--teal); }

  .hero { position: absolute; top: 58px; left: 0; width: 780px; height: 196px; }

  .section-title { position: absolute; top: 281px; width: 780px; text-align: center; font-size: 18px; font-weight: 700; color: var(--ink); letter-spacing: 0.3px; }

  .tabs { position: absolute; top: 328px; left: 276px; display: flex; }
  .tab { height: 24px; padding: 0 15px; font-size: 8.5px; font-weight: 700; color: var(--ink); line-height: 24px; margin-right: 12px; }
  .tab.is-active { background: var(--teal); color: var(--white); width: 68px; text-align: center; padding: 0; margin-right: 14px; }

  .photo { background: linear-gradient(135deg, var(--hero-a), var(--hero-b)); }
  .featured-photo { position: absolute; left: 49px; top: 381px; width: 391px; height: 241px; background: linear-gradient(160deg, #cdb48e 0%, #d5c2a3 45%, #8fb2b8 100%); }
  .category-tag { position: absolute; left: 11px; top: 13px; background: var(--pink); color: var(--white); font-size: 9px; font-weight: 700; padding: 0 8px; height: 20px; line-height: 20px; }
  .featured-text { position: absolute; left: 458px; top: 378px; width: 276px; }
  .post-title { color: var(--teal-dark); font-weight: 700; text-transform: uppercase; }
  .featured-text .post-title { font-size: 12px; line-height: 18.5px; }
  .featured-text p { font-size: 10.4px; line-height: 19.2px; margin-top: 9px; }

  .btn-read { display: inline-block; background: var(--pink); color: var(--white); font-size: 9px; font-weight: 700; text-align: center; text-decoration: none; }
  .featured-text .btn-read { position: absolute; left: 0; top: 212px; width: 99px; height: 32px; line-height: 32px; }

  .card { position: absolute; top: 666px; width: 214px; }
  .card .photo { height: 128px; }
  .card .post-title { font-size: 12px; line-height: 18.5px; margin-top: 14px; }
  .card p { font-size: 9px; line-height: 15.6px; margin-top: 10px; }
  .card .btn-read { position: absolute; top: 261px; left: 0; width: 99px; height: 32px; line-height: 32px; }

  .btn-view-all { position: absolute; left: 302px; top: 1006px; width: 176px; height: 30px; border: 2px solid var(--teal); color: var(--teal); font-size: 9px; font-weight: 700; text-align: center; line-height: 26px; }

  .site-footer { position: absolute; left: 0; top: 1066px; width: 780px; height: 134px; }
  .signup { position: absolute; top: 28px; left: 234px; display: flex; align-items: center; }
  .signup-label { color: var(--white); font-size: 12px; font-weight: 700; margin-right: 7px; }
  .signup-input { width: 188px; height: 28px; background: var(--white); font-size: 8.5px; color: var(--ink); line-height: 28px; padding-left: 10px; }
  .signup-btn { width: 32px; height: 28px; background: var(--pink); display: flex; align-items: center; justify-content: center; }
  .copyright { position: absolute; top: 78px; width: 780px; text-align: center; color: #cfcfcf; font-size: 7.5px; }
  .social { position: absolute; top: 96px; left: 334px; display: flex; gap: 14px; }
  .social span { width: 12px; height: 12px; border-radius: 50%; background: #d9d9d9; }
</style>
</head>
<body>

<header class="site-header">
  <div class="brand">BRIGHTYEARSAHEAD</div>
  <nav class="main-nav">
    <a class="is-current" href="#">HOME</a>
    <a href="#">FASHION</a>
    <a href="#">FEELINGS</a>
    <a href="#">FITNESS</a>
    <a href="#">CONTACT</a>
  </nav>
</header>

<svg class="hero" width="780" height="196" viewBox="0 0 780 196" role="img" aria-label="Slider photo: smiling blonde woman in front of a colourful painted wall">
  <defs>
    <linearGradient id="heroFill" x1="0" y1="0" x2="1" y2="0">
      <stop offset="0" stop-color="#c9b7a0"/>
      <stop offset="0.45" stop-color="#e2c7a6"/>
      <stop offset="1" stop-color="#b8ad9b"/>
    </linearGradient>
  </defs>
  <rect width="780" height="196" fill="url(#heroFill)"/>
  <path d="M0 150 Q390 260 780 138 L780 196 L0 196 Z" fill="#ffffff"/>
</svg>

<h2 class="section-title">FEATURED BLOG POSTS</h2>

<div class="tabs">
  <div class="tab is-active">FASHION</div>
  <div class="tab">FEELINGS</div>
  <div class="tab">FITNESS</div>
</div>

<article class="featured">
  <div class="featured-photo" role="img" aria-label="Photo: laughing woman in a straw sun hat and sunglasses by the sea">
    <span class="category-tag">FASHION</span>
  </div>
  <div class="featured-text">
    <h3 class="post-title">Lorem ipsum dolor sit amet vitae dicta sunt explicabo. Nemo enim ipsam</h3>
    <p>Duis aute irure dolor in reprehenderit in voluptate velit esse cillum dolore eu fugiat nulla pariatur. Excepteur sint occaecat cupidatat non proident, sunt in culpa qui officia deserunt mollit anim id est laborum consectetur adipisicing elit, sed do eiusmod tempor incididunt ut labore et doloreasdes magna aliqua. Ut enim ad minim veniam, quis nostrud exercitation ullamco laboris nisi ut aliquip ex ea commodalo consequat.</p>
    <a class="btn-read" href="#">READ MORE</a>
  </div>
</article>

<article class="card" style="left:49px">
  <div class="photo" role="img" aria-label="Photo: woman in sunglasses riding a red scooter" style="background:linear-gradient(160deg,#9fb08a,#d9d3c4 55%,#c94a4a)"></div>
  <h3 class="post-title">Lorem ipsum dolor sit amet vitae dicta sunt...</h3>
  <p>Duis aute irure dolor in reprehenderit in voluptate velit esse cillum dolore eu fugiat nulla pariatur. Excepteur sint occaecat cupidatat non proident, sunt in culpa qui officia...</p>
  <a class="btn-read" href="#">READ MORE</a>
</article>

<article class="card" style="left:282px">
  <div class="photo" role="img" aria-label="Photo: woman in sunglasses relaxing on a bench at sunset" style="background:linear-gradient(160deg,#e9c78f,#c89a63 55%,#6f5a45)"></div>
  <h3 class="post-title">Lorem ipsum dolor sit amet vitae dicta sunt...</h3>
  <p>Duis aute irure dolor in reprehenderit in voluptate velit esse cillum dolore eu fugiat nulla pariatur. Excepteur sint occaecat cupidatat non proident, sunt in culpa qui officia...</p>
  <a class="btn-read" href="#">READ MORE</a>
</article>

<article class="card" style="left:517px">
  <div class="photo" role="img" aria-label="Photo: woman in a magenta dress beside a lit dressing mirror" style="background:linear-gradient(90deg,#6a4a36,#9b2a5f 45%,#5c3f2c)"></div>
  <h3 class="post-title">Lorem ipsum dolor sit amet vitae dicta sunt...</h3>
  <p>Duis aute irure dolor in reprehenderit in voluptate velit esse cillum dolore eu fugiat nulla pariatur. Excepteur sint occaecat cupidatat non proident, sunt in culpa qui officia...</p>
  <a class="btn-read" href="#">READ MORE</a>
</article>

<div class="btn-view-all">VIEW ALL FASHION POSTS</div>

<footer class="site-footer">
  <svg width="780" height="134" viewBox="0 0 780 134" style="position:absolute;left:0;top:0">
    <path d="M0 56 Q390 -40 780 56 L780 134 L0 134 Z" fill="var(--footer)"/>
  </svg>
  <div class="signup">
    <span class="signup-label">EMAIL SIGN UP</span>
    <div class="signup-input">Enter Email Address</div>
    <div class="signup-btn">
      <svg width="13" height="10" viewBox="0 0 13 10"><rect x="0" y="0" width="13" height="10" rx="1" fill="#fff"/><path d="M0.5 1 L6.5 5.5 L12.5 1" stroke="var(--pink)" stroke-width="1.3" fill="none"/></svg>
    </div>
  </div>
  <div class="copyright">Copyright © 2018, Company Name All Right reserved</div>
  <div class="social" aria-label="Social media links">
    <span></span><span></span><span></span><span></span><span></span>
  </div>
</footer>

</body>
</html>
```